IT services web page design

Hello!

We need new design for our web site, obviously :)

Our company is service oriented and we are maintaining, configuring and fixing problems for IT + selling other internet related services.

Our speciality are in area of internet services (web, dns, email, databases, backup...) and internet servers technology.

We also provide service and sales of Zentro Apps and Veltrania Quillbox365 for which we are certified by Zentro and Veltrania.

Other services that we provide (not so in focus) are: VPS hosting, remote backup, web hosting, pagemoss fixing...

People mostly call us when they have a problems and this is core idea that new web site has to communicate - We can fix your server / web / email problems, save your money and as* :)

Our team have 15+ years experience with all range of internet technology + bunch of certificates from Veltrania and Durvo [we need to show people we have certificates].
Our qualities: experience, knowledge, delivery on time

In start we will not have blog section, but we need it in future. We also need place for flonkit feeds on web site.

Depth of the site should be max. level 2.

This site will go out in two languages so we need switch button on page from pone language to another.

Target Market(s)

small and mid size business that use internet services for daily operations and main business

Industry/Entity Type

Internet

Requirements
Must have
• * design should be in the way that responsive web could be made

Nice to have
• Long format will be OK for us. Like today pages that list all services and benefits on one loooong web page...

Logo is in attachment. It will be nice to have it on web site but if you find it not appropriate you can change it or put another one.

```html
<!DOCTYPE html>
<html lang="en">
<head>
<meta charset="utf-8">
<title>Kestrel grupa – IT Solutions</title>
<link href="https://fonts.googleapis.com/css2?family=PT+Sans+Narrow:wght@400;700&family=Source+Sans+3:wght@400;700&display=swap" rel="stylesheet">
<style>
:root{
  --page:#f3f2f2;
  --ink:#333333;
  --muted:#555555;
  --nav-top:#6fb8e8;
  --nav-bottom:#3d93d4;
  --green-dark:#3f8a17;
  --green-mid:#6aab25;
  --green-light:#8cc63f;
  --footer:#4d4d4d;
  --accent-blue:#1d5fa6;
  --more-red:#b3262b;
  --card-line:#dcdcdc;
  --button-green:#4f8a12;
}
*{box-sizing:border-box;margin:0;padding:0}
html,body{width:1140px;height:1200px;overflow:hidden}
body{position:relative;background:var(--page);font-family:"Source Sans 3",Arial,sans-serif;color:var(--ink)}
.abs{position:absolute}
.heading{font-family:"PT Sans Narrow","Arial Narrow",sans-serif;text-transform:uppercase}

/* header */
.brand{left:131px;top:28px;display:flex;align-items:center;gap:10px}
.brand-name{font-weight:700;font-size:27px;color:#1a1a1a;line-height:1}
.brand-tag{font-size:8px;letter-spacing:3px;font-weight:700;color:#1a1a1a;display:block;margin-top:2px;margin-left:22px}
.brand-mark{width:56px;height:56px;border-radius:50%;background:#5a9a3a}
.search{left:682px;top:25px;width:163px;height:20px;display:flex;border:1px solid #cfcfcf;background:#fff}
.search span{flex:1;font-size:12px;font-style:italic;color:#777;padding:3px 10px}
.search b{width:28px;background:#2f6fa0;display:flex;align-items:center;justify-content:center}
.lang{left:867px;top:25px;width:144px;height:21px;border:1px solid #cfcfcf;background:#fff;display:flex;align-items:center;gap:8px;padding:0 8px;font-size:11px;font-style:italic;color:#888}
.lang i{width:18px;height:11px;background:#6a7fb0;display:block}
.lang svg{margin-left:auto}
.phone{left:686px;top:63px;display:flex;align-items:center;gap:6px;font-size:16px;color:#333}

/* navigation */
.nav{left:0;top:105px;width:1140px;height:43px;background:linear-gradient(var(--nav-top),var(--nav-bottom));border-bottom:2px solid #a9d3f0}
.nav a{position:absolute;top:0;height:41px;line-height:41px;color:#fff;text-decoration:none;font-size:15.5px;white-space:nowrap}
.nav .sep{position:absolute;top:0;width:1px;height:41px;background:#8cc6ee}

/* hero */
.band{left:0;top:148px;width:1140px;height:312px;background:radial-gradient(ellipse at 80% 55%,var(--green-light),var(--green-mid) 40%,var(--green-dark))}
.slider{left:116px;top:177px;width:912px;height:314px;background:#e6e6e6;border-radius:3px}
.slide{left:124px;top:186px;width:896px;height:295px;background:#fff}
.slide-art{left:318px;top:186px;width:508px;height:295px;background:linear-gradient(160deg,#f4f7f9,#cfe3ee 60%,#e8eef2)}
.caption{left:124px;top:280px;width:320px;height:132px;background:rgba(88,88,88,.93);color:#fff;padding:18px 21px}
.caption h2{font-family:"PT Sans Narrow",sans-serif;font-weight:400;font-size:19px;border-bottom:1px solid #ccc;padding-bottom:4px;margin-bottom:8px;display:inline-block}
.caption p{font-size:12.5px;line-height:20px;width:245px}
.dots{left:512px;top:455px;width:116px;height:26px;background:#eee;border-radius:6px 6px 0 0;display:flex;gap:13px;justify-content:center;align-items:center}
.dots i{width:13px;height:13px;border-radius:50%;background:#8c8c8c;border:2px solid #d6d6d6}
.dots i.on{background:#3b7bb8}

/* intro */
.welcome{left:125px;top:516px;font-size:21px;color:#333}
.welcome em{font-style:normal;color:var(--accent-blue);margin-left:4px}
.intro{left:126px;top:550px;width:920px;font-size:10.5px;line-height:23px;color:#333}

/* service cards */
.card{width:270px;height:118px;border:1px solid var(--card-line);background:linear-gradient(#fff,#f3f3f3);padding:0 11px}
.card h3{font-family:"PT Sans Narrow",sans-serif;font-weight:400;font-size:16px;color:#333;margin-top:17px;white-space:nowrap}
.card p{width:150px;font-size:11.5px;line-height:18px;text-align:justify;margin-top:6px;color:#333}
.card .art{position:absolute;right:14px;top:42px;width:82px;height:44px;background:linear-gradient(#eceff2,#c7ccd2);border-radius:3px}
.card .more{position:absolute;right:22px;bottom:11px;font-family:"PT Sans Narrow",sans-serif;font-size:13px;color:var(--more-red)}

/* footer */
.footer-shape{left:0;top:940px}
.footer-title{font-size:20px;color:#fff;border-bottom:1px solid #888;padding-bottom:3px}
.news-date{left:130px;top:1066px;width:250px;font-size:11px;line-height:16px;color:#eee;text-align:justify}
.btn-more{left:317px;top:1140px;width:66px;height:27px;background:var(--button-green);border-radius:4px;color:#fff;font-size:11.5px;font-weight:700;text-align:center;line-height:26px}
.news-text{left:436px;top:1054px;width:250px;font-size:11px;line-height:16px;color:#ddd}
.email{left:439px;top:1104px;width:245px;height:30px;background:#fff;border:1px solid #ccc;border-radius:3px;font-size:11px;font-style:italic;color:#888;padding:7px 15px}
.subscribe{left:584px;top:1150px;width:100px;height:31px;background:var(--button-green);color:#fff;font-family:"PT Sans Narrow",sans-serif;font-size:15px;text-align:center;line-height:31px}
.social{left:792px;top:1027px;display:flex;gap:12px}
.social i{width:25px;height:25px;background:#6e7f8f;border:1px solid #8d9aa6;display:block}
.copy{left:794px;top:1070px;font-size:11px;color:#ddd}
</style>
</head>
<body>

<header>
  <div class="abs brand">
    <div><span class="brand-name">Kestrel grupa</span><span class="brand-tag">IT SOLUTIONS</span></div>
    <span class="brand-mark"></span>
  </div>
  <div class="abs search"><span>Search</span><b><svg width="11" height="11" viewBox="0 0 11 11"><circle cx="4.5" cy="4.5" r="3.3" fill="none" stroke="#fff" stroke-width="1.6"/><line x1="7" y1="7" x2="10" y2="10" stroke="#fff" stroke-width="1.8"/></svg></b></div>
  <div class="abs lang"><i></i>English<svg width="8" height="5" viewBox="0 0 8 5"><path d="M1 1l3 3 3-3" fill="none" stroke="#555" stroke-width="1.2"/></svg></div>
  <div class="abs phone">
    <svg width="20" height="26" viewBox="0 0 20 26"><path d="M5 1c-3 1-4 3-4 6 1 7 5 14 11 17 2 1 4 1 6-1l-4-5-3 2C8 17 6 13 6 10l3-2L5 1z" fill="#3a3a3a"/></svg>
    385 91 4080 517
  </div>
</header>

<nav class="abs nav heading">
  <a style="left:130px">Home</a><span class="sep" style="left:191px"></span>
  <a style="left:212px">Virtual Private Server (VPS)</a><span class="sep" style="left:410px"></span>
  <a style="left:427px">Maintenance of Computer Systems</a><span class="sep" style="left:660px"></span>
  <a style="left:681px">Zentro Apps</a><span class="sep" style="left:777px"></span>
  <a style="left:804px">Hosting Services</a><span class="sep" style="left:923px"></span>
  <a style="left:953px">Contact</a>
</nav>

<section>
  <div class="abs band"></div>
  <div class="abs slider"></div>
  <div class="abs slide"></div>
  <div class="abs slide-art" role="img" aria-label="Illustration of servers and workstations connected to a central hub behind a brick firewall"></div>
  <div class="abs caption">
    <h2>LOREM IPSUM DOLOR SIT AMET, ELIT</h2>
    <p>Cum sociis natoque penatibus et magnis dis parturient montes, nascetur ridiculus mus. In iaculis facilisis massa. Etiam eu urna. Sed porta.</p>
  </div>
  <div class="abs dots"><i></i><i></i><i class="on"></i><i></i></div>
</section>

<section>
  <h1 class="abs welcome heading" style="font-weight:400">Welcome to <em>kestrel-grupa.com</em></h1>
  <div class="abs intro">
    <p>We are a company that configures and maintains web servers and builds advanced IT solutions to support their business.</p>
    <p>Our clients are companies that uses its advanced IT solutions in the form of dedicated servers, virtual servers (VPS), private networks (VPN) and online backup on Fenstra and Durvo platforms.</p>
    <p>As an added value services are available for 00-24 resolved, the removal of all the problems in order to ensure smooth operation of the services and related services.</p>
    <p>We have the knowledge and 15 + years of experience in the field of installation, configuration and maintenance services such as:</p>
  </div>

  <div class="abs card" style="left:129px;top:670px"><h3>FENSTRA SERVERS</h3><p>Sed ut perspiciatis unde omnis iste natus error sit voluptatem laudantium.</p><span class="art" role="img" aria-label="Server operating system product image"></span><span class="more">MORE &gt;&gt;</span></div>
  <div class="abs card" style="left:434px;top:670px"><h3>DURVO SERVERI</h3><p>Sed ut perspiciatis unde omnis iste natus error sit voluptatem laudantium.</p><span class="art" role="img" aria-label="Server rack illustration"></span><span class="more">MORE &gt;&gt;</span></div>
  <div class="abs card" style="left:739px;top:670px"><h3>WEB SERVISI</h3><p>Sed ut perspiciatis unde omnis iste natus error sit voluptatem laudantium.</p><span class="art" role="img" aria-label="Web address lettering illustration"></span><span class="more">MORE &gt;&gt;</span></div>
  <div class="abs card" style="left:129px;top:804px"><h3>DNS AND DOMAIN</h3><p>Sed ut perspiciatis unde omnis iste natus error sit voluptatem laudantium.</p><span class="art" role="img" aria-label="Domain name illustration"></span><span class="more">MORE &gt;&gt;</span></div>
  <div class="abs card" style="left:434px;top:804px"><h3>EMAIL SERVISI</h3><p>Sed ut perspiciatis unde omnis iste natus error sit voluptatem laudantium.</p><span class="art" role="img" aria-label="Email server appliance image"></span><span class="more">MORE &gt;&gt;</span></div>
  <div class="abs card" style="left:739px;top:804px"><h3>FIREWALL AND VPN SOLUTIONS</h3><p>Sed ut perspiciatis unde omnis iste natus error sit voluptatem laudantium.</p><span class="art" role="img" aria-label="VPN connection illustration with folders"></span><span class="more">MORE &gt;&gt;</span></div>
</section>

<footer>
  <svg class="abs footer-shape" width="1140" height="260" viewBox="0 0 1140 260">
    <path d="M340 62 C600 20 900 -2 1140 7 L1140 50 C900 40 620 45 340 62Z" fill="#7fb51f"/>
    <path d="M0 50 C150 62 260 66 380 62 C650 52 900 40 1140 50 L1140 260 L0 260Z" fill="var(--footer)"/>
  </svg>
  <h2 class="abs heading footer-title" style="left:127px;top:1022px;width:242px;font-weight:400">Latest News</h2>
  <div class="abs news-date">June 27 2013<br>Sed ut perspiciatis unde omnis iste natus error sit voluptatem accusantium doloremque laudantium, totam rem aperiam, eaque ipsa quae ab illo inven.</div>
  <div class="abs btn-more">More &gt;&gt;</div>

  <h2 class="abs heading footer-title" style="left:441px;top:1022px;width:243px;font-weight:400">Newsletter</h2>
  <div class="abs news-text" style="top:1056px">Sed ut perspiciatis unde omnis iste natus error sit voluptatem accusantium doloremque la.</div>
  <div class="abs email">Your Email Id</div>
  <div class="abs subscribe">Subscribe</div>

  <div class="abs social"><i></i><i></i><i></i><i></i><i></i><i></i></div>
  <div class="abs copy">© 2013 Kestrel-grupa.com., All rights reserved</div>
</footer>

</body>
</html>
```